Create a book cover - front, back and spine - for a book aimed at high school and college graduates. The book poses a series of questions and possible ways of answering these questions.

Size 5" x 8" with a .45" spine.

Target Market(s)

18-25 year old high school and college graduates.

Industry/Entity Type

High School

Requirements
Must have
• Front cover - image(s) related to graduation, text "Seven Crossroads Before Your Next Chapter" and the author "Tomas Quillan"

Back cover - see attachment. Text will be altered later but right now I just need filler spots.

```html
<!DOCTYPE html>
<html lang="en">
<head>
<meta charset="utf-8">
<title>Seven Crossroads Before Your Next Chapter – Cover Spread</title>
<link href="https://fonts.googleapis.com/css2?family=Cabin:wght@400;600;700&display=swap" rel="stylesheet">
<style>
  :root {
    --page: #ffffff;
    --cover: #ffffff;
    --frame: #b9bcc2;
    --box-line: #8a8a8a;
    --ink: #141414;
    --teal: #1e6462;
    --red: #c0181f;
    --cap: #1d1d1f;
    --globe: #5f7fa6;
    --book: #4c6480;
    --haze: #eef1f5;
  }
  * { margin: 0; padding: 0; box-sizing: border-box; }
  html, body {
    width: 1200px; height: 961px; overflow: hidden;
    background: var(--page);
    font-family: "Cabin", sans-serif;
    color: var(--ink);
  }
  .spread {
    position: absolute; left: 42px; top: 78px;
    width: 1139px; height: 871px;
    background: var(--cover);
    border: 1px solid var(--frame);
  }

  /* Back cover */
  .back { position: absolute; left: 29px; top: 50px; width: 488px; }
  .back-title { color: var(--teal); font-size: 16.5px; font-weight: 400; margin-bottom: 13px; }
  .blurb {
    font-size: 16.8px; line-height: 22.2px; text-align: justify;
    text-indent: 26px; margin-bottom: 20px;
  }
  .quote { margin-bottom: 20px; font-size: 16.8px; line-height: 22.2px; }
  .quote p { text-align: justify; }
  .quote cite { display: block; font-style: normal; color: var(--teal); }
  .barcode-box {
    position: absolute; left: 300px; top: 755px;
    width: 210px; height: 88px;
    border: 1px solid var(--box-line);
    display: flex; align-items: center; justify-content: center;
    font-size: 17px; color: var(--ink);
  }

  /* Spine */
  .spine-title, .spine-author {
    position: absolute; left: 558px;
    writing-mode: vertical-rl;
    font-size: 21px; white-space: nowrap; color: var(--ink);
  }
  .spine-title { top: 50px; }
  .spine-author { top: 708px; }

  /* Front cover */
  .front { position: absolute; left: 585px; top: 0; width: 554px; height: 871px; }
  .front-title {
    position: absolute; top: 48px; left: 0; width: 100%;
    text-align: center; font-weight: 700; line-height: 1;
    text-shadow: 2px 2px 3px rgba(0,0,0,0.35);
  }
  .front-title .lead { display: block; font-size: 47px; line-height: 58px; }
  .front-title .key {
    display: block; font-size: 124px; color: var(--red);
    margin-top: 0; letter-spacing: 1px; line-height: 120px;
    -webkit-text-stroke: 1.5px #2a0a0a;
  }
  .cover-art {
    position: absolute; left: 86px; top: 354px; width: 440px; height: 376px;
    border-radius: 12px;
    background:
      radial-gradient(ellipse 55% 45% at 62% 62%, rgba(95,127,166,0.95) 0%, rgba(95,127,166,0) 100%),
      linear-gradient(180deg, var(--cap) 0%, #3a3d44 22%, var(--globe) 45%, #7894b6 68%, var(--book) 86%, var(--haze) 100%);
  }
  .front-author {
    position: absolute; right: 51px; top: 807px;
    font-size: 28px; line-height: 32px; color: var(--red);
  }
</style>
</head>
<body>
<main class="spread">
  <section class="back">
    <h2 class="back-title">Seven Crossroads Before Your Next Chapter</h2>
    <p class="blurb">This graduation gift is blah dog and cat and now is the time for all good men to come to the aid of their countries and sometimes when it rains it pours and then there are other words that are interesting and they come next and then we put in a period. This period shows that there are different sentences, and probably I’ll put a bit more thought into this summary paragraph at some point, but right now it’s just not a priority so I’m sticking with this for now, but within the week it should be all done and we can make the adjustments at that point.</p>
    <blockquote class="quote">
      <p>“This was one of the best books I ever read because it had consonants and vowels and a variety of punctuation marks!”</p>
      <cite>Dana Whitlock, Gulf Coast University – Class of 2013</cite>
    </blockquote>
    <blockquote class="quote">
      <p>“If only I’d have answered these questions after I’d graduated, I might not be living in my parents basement trying to invent a new synonym for ‘fetch’”</p>
      <cite>Ashlyn Marrow, Very Important College – Class of 2046</cite>
    </blockquote>
    <blockquote class="quote">
      <p>“This book has just the right balance of history and economics and totally made up stuff that it makes his theories both palpable and alluring to Type 1 Diabetics and furniture salesmen.”</p>
      <cite>Abel Corvino, Linden Park University – Class of 2008</cite>
    </blockquote>
    <blockquote class="quote">
      <p>“A great book! I’ll read it in a few weeks if I have nothing else to do! I likeexclamation marks!”</p>
      <cite>Sadie Sumner, Cedar Ridge High School, Class of 2012</cite>
    </blockquote>
  </section>
  <div class="barcode-box">Bar Code</div>

  <div class="spine-title">Seven Crossroads Before Your Next Chapter</div>
  <div class="spine-author">Tomas Quillan</div>

  <section class="front">
    <h1 class="front-title">
      <span class="lead">Seven Crossroads</span>
      <span class="lead">Before Your Next</span>
      <span class="key">Chapter</span>
    </h1>
    <div class="cover-art" role="img" aria-label="Graduation illustration: a black mortarboard cap with a gold tassel resting on a blue globe, which sits on a slate-blue book, beside a rolled diploma tied with a red ribbon and a large numeral"></div>
    <p class="front-author">Tomas Quillan</p>
  </section>
</main>
</body>
</html>
```